Voltline Assemblies, Inc. Business Card

Voltline has three operating entities and I'm looking for a standard business card template that can be used for Voltline and the three operating entities that the logo just get swapped out, but has a very similar look and feel. Ultimately if someone had a business card from each, they assume the organizations are related because they all have the same look and feel.
Below are our websites and I will attached the logos for each entity:
https://www.voltlineassemblies.example/
https://www.brantoceramic.example/
https://www.omra-kfsd.example/
https://www.summitbreaker.example/

Target Market(s)

US Voltline

Industry/Entity Type

US Voltline

Contact Information for Business Card

Normal stuff

```html
<!DOCTYPE html>
<html lang="en">
<head>
<meta charset="utf-8">
<title>Voltline Assemblies, Inc. – Business Card</title>
<link rel="stylesheet" href="https://fonts.googleapis.com/css2?family=Montserrat:wght@400;500;700;800&display=swap">
<style>
  :root {
    --navy: #1f2d6b;
    --navy-light: #2c3d8a;
    --navy-dark: #18235a;
    --red: #c8192e;
    --ink: #1a1a1a;
    --paper: #ffffff;
    --backdrop: #e4e5e9;
  }
  * { box-sizing: border-box; margin: 0; padding: 0; }
  html, body {
    width: 1200px; height: 900px; overflow: hidden;
    background: var(--backdrop);
    font-family: "Montserrat", sans-serif;
  }
  .card {
    position: absolute;
    width: 700px; height: 400px;
    border-radius: 20px; overflow: hidden;
    box-shadow: 0 10px 26px rgba(0,0,0,.2);
  }
  .card-front { left: 60px; top: 40px; background: var(--paper); }
  .card-back { left: 440px; top: 470px; background: var(--navy); }

  .card-swoosh { position: absolute; inset: 0; }
  .brand {
    position: absolute; left: 45px; top: 100px; width: 290px;
    display: flex; align-items: center; gap: 12px;
  }
  .brand-dot {
    flex: none; width: 46px; height: 46px; border-radius: 50%;
    background: var(--navy);
  }
  .brand-name {
    color: var(--navy); font-weight: 800; font-size: 23px;
    line-height: 1.1; letter-spacing: .3px; text-transform: uppercase;
  }
  .divider {
    position: absolute; left: 358px; top: 100px;
    width: 2px; height: 165px; background: var(--navy);
  }
  .contact { position: absolute; left: 380px; top: 96px; color: var(--ink); }
  .contact-name {
    color: var(--red); font-weight: 800; font-size: 27px;
    line-height: 1.15; text-transform: uppercase; letter-spacing: .3px;
  }
  .contact-role { font-size: 15px; font-weight: 500; margin-bottom: 12px; }
  .contact-address { font-size: 14px; line-height: 1.4; margin-bottom: 10px; }
  .contact-list { list-style: none; font-size: 14px; line-height: 1.6; }
  .contact-list li { display: flex; align-items: center; gap: 7px; }
  .contact-list svg { width: 12px; height: 12px; flex: none; }

  .back-pattern {
    position: absolute; inset: 0;
    background: radial-gradient(ellipse at 30% 30%, var(--navy-light), var(--navy) 55%, var(--navy-dark));
  }
  .back-brand {
    position: absolute; right: 30px; bottom: 28px;
    display: flex; align-items: center; gap: 10px;
  }
  .back-brand-dot {
    width: 40px; height: 40px; border-radius: 50%; background: var(--paper);
  }
  .back-brand-name {
    color: var(--paper); font-weight: 800; font-size: 16px;
    text-transform: uppercase; letter-spacing: .3px;
  }
</style>
</head>
<body>
  <article class="card card-front">
    <svg class="card-swoosh" viewBox="0 0 700 400" preserveAspectRatio="none" aria-hidden="true">
      <path d="M0 170 C 60 270, 300 345, 700 372 L700 400 L0 400 Z" fill="var(--navy)"/>
      <path d="M50 228 C 170 300, 400 352, 700 365" fill="none" stroke="var(--red)" stroke-width="6"/>
      <path d="M0 174 C 60 272, 300 347, 700 369" fill="none" stroke="var(--paper)" stroke-width="4"/>
    </svg>

    <div class="brand">
      <span class="brand-dot"></span>
      <span class="brand-name">Voltline Assemblies, Inc.</span>
    </div>

    <div class="divider"></div>

    <section class="contact">
      <h1 class="contact-name">Dorian Hale</h1>
      <p class="contact-role">Director</p>
      <p class="contact-address">2840 W Marlow,<br>Fenwick, Oklahoma 74009</p>
      <ul class="contact-list">
        <li>
          <svg viewBox="0 0 18 18"><rect x="4" y="1" width="10" height="16" rx="2" fill="none" stroke="var(--red)" stroke-width="2"/></svg>
          555-300-0147
        </li>
        <li>
          <svg viewBox="0 0 18 18"><rect x="1" y="3" width="16" height="12" fill="var(--red)"/><path d="M1 3 L9 10 L17 3" fill="none" stroke="#fff" stroke-width="1.5"/></svg>
          info@voltlineassemblies.example
        </li>
        <li>
          <svg viewBox="0 0 18 18"><circle cx="9" cy="9" r="8" fill="var(--red)"/><path d="M1 9 H17 M9 1 C4 6,4 12,9 17 M9 1 C14 6,14 12,9 17" fill="none" stroke="#fff" stroke-width="1.2"/></svg>
          www.voltlineassemblies.example
        </li>
      </ul>
    </section>
  </article>

  <article class="card card-back">
    <div class="back-pattern" role="img" aria-label="Repeating embossed brand pattern in tonal navy"></div>
    <div class="back-brand">
      <span class="back-brand-dot"></span>
      <span class="back-brand-name">Voltline</span>
    </div>
  </article>
</body>
</html>
```